Bluebell Therapy Services needs upgraded website

Upgrade current website www.bluebelltherapy.com.au. Need to incorporate new logo (attached). Family friendly and professional feel. Use of colour green. We are based in Melbourne, Australia and work with children aged 0-16 who have additional needs requiring therapy.

Target Market(s)

Parents of children with special needs.

Industry/Entity Type

Work

Colors
000000

Requirements
Must have
• The current content/ pictures are already on the website and can be replicated, just with a fresh look. Additionally need an FAQ section. Must incorporate logo and have consistency on each page. Needs to be accessible on tablets/devices (current website only shows home page on devices, however actual sites has many sub pages (approx. 7). I will need to be able to easily edit the content down the track and potentially add pages.

```html
<!DOCTYPE html>
<html lang="en">
<head>
<meta charset="utf-8">
<title>Bluebell Therapy Services</title>
<link href="https://fonts.googleapis.com/css2?family=Roboto:ital,wght@0,400;0,500;0,700;1,700&display=swap" rel="stylesheet">
<style>
:root{
  --green:#3fa845;
  --green-dark:#1f6a25;
  --green-deep:#174f1b;
  --ink:#222;
  --muted:#555;
  --grey-bg:#ececec;
  --white:#fff;
}
*{box-sizing:border-box;margin:0;padding:0}
html,body{width:1200px;height:2911px;overflow:hidden}
body{font-family:'Roboto',sans-serif;color:var(--ink);background:var(--white);position:relative}
.abs{position:absolute}
.photo{position:absolute}

/* brand lockup */
.brand{display:flex;align-items:center;gap:12px}
.brand .mark{width:30px;height:30px;background:var(--white);flex:none}
.brand .name{color:var(--white);font-size:26px;font-weight:700;letter-spacing:.5px;white-space:nowrap}

/* header */
.topbar{top:0;left:0;width:1200px;height:90px;background:var(--green)}
.topbar .contact{left:84px;top:20px;color:var(--white);font-size:13px;line-height:20px}
.topbar .brand{left:450px;top:20px}
.topbar .right{right:84px;top:18px;color:var(--white);font-size:13px;text-align:right;line-height:22px}
.topbar .right a{color:var(--white);text-decoration:none;margin-left:22px}
.nav{top:90px;left:0;width:1200px;height:52px;background:rgba(30,80,30,.55);display:flex;justify-content:center;align-items:center;gap:34px;z-index:2}
.nav a{color:var(--white);font-size:13px;font-weight:500;text-decoration:none;display:flex;align-items:center;gap:7px}
.nav a::before{content:"";width:7px;height:7px;border-radius:50%;background:var(--green)}

/* hero */
.hero{top:90px;left:0;width:1200px;height:525px;background:linear-gradient(120deg,#c9b79e 0%,#e6dccd 35%,#b69a7c 65%,#7a6a58 100%)}
.hero .welcome{left:0;top:395px;width:1200px;height:130px;background:linear-gradient(rgba(40,60,30,0),rgba(30,45,25,.55));text-align:center;color:var(--white)}
.welcome h1{font-size:30px;font-weight:700;margin-top:2px}
.welcome p{width:700px;margin:8px auto 0;font-size:15px;line-height:21px}

/* services */
.svc{width:230px}
.svc h2{font-size:18px;color:var(--green-dark);font-weight:700;margin-bottom:12px}
.svc .pic{position:relative;height:153px;border:4px solid #ddd}
.svc p{font-size:12px;color:var(--muted);line-height:17px;margin-top:14px;height:52px}
.btn{display:inline-block;margin-top:12px;background:var(--green-deep);color:var(--white);font-size:11px;font-weight:700;padding:7px 12px;text-decoration:none}
.ot{left:660px;top:712px;width:456px}
.ot h2{font-size:19px;color:var(--green-dark);margin-bottom:14px}
.ot p{font-size:12px;line-height:17px;color:var(--muted)}
.ot ul{list-style:none;margin-top:16px}
.ot li{font-size:12px;font-weight:700;color:var(--green-dark);margin-bottom:12px;padding-left:18px;position:relative}
.ot li::before{content:"";position:absolute;left:0;top:4px;width:6px;height:6px;background:var(--green)}
.ot-photo{left:660px;top:1100px;width:456px;height:320px;border:4px solid #ddd;background:linear-gradient(135deg,#e2d9c8,#b7a48e 55%,#c33a2a 85%)}

/* staff band */
.staff{top:1445px;left:0;width:1200px;height:375px;background:linear-gradient(90deg,#6d5a4a,#a79078 45%,#5a4a40)}
.card{top:75px;width:224px;height:250px;border:4px solid rgba(255,255,255,.85)}
.card .pic{position:absolute;inset:0}
.card .label{position:absolute;left:0;right:0;bottom:0;height:34px;background:rgba(0,0,0,.55);color:var(--white);font-size:13px;font-weight:500;display:flex;align-items:center;justify-content:center}

/* feature boxes */
.features{top:1827px;left:0;width:1200px;height:260px;background:var(--grey-bg)}
.fbox{top:73px;width:302px;height:144px;background:var(--white);border:3px solid #d8d8d8;padding:18px 18px}
.fbox h3{font-size:16px;color:var(--green-dark);font-weight:700;margin-bottom:10px}
.fbox p{font-size:12px;line-height:17px;color:var(--muted)}
.fbox a{display:block;margin-top:14px;font-size:11px;color:var(--green-dark);text-decoration:underline}

/* articles */
.section-title{font-size:19px;font-weight:700;color:var(--green-dark)}
.article{top:2152px;width:246px;height:258px;border:6px solid var(--green-deep);background:var(--green-deep)}
.article .pic{position:absolute;left:0;top:0;right:0;height:170px}
.article .cap{position:absolute;left:0;right:0;bottom:0;height:76px;color:var(--white);font-size:15px;font-weight:700;display:flex;align-items:center;justify-content:center;text-align:center;line-height:20px}
.services-list{left:893px;top:2152px;width:223px;list-style:none}
.services-list li{font-size:12px;color:var(--ink);padding:6px 0 8px;border-bottom:1px solid #e3e3e3}
.services-list li.active{color:var(--green);font-weight:700}

/* quote */
.quote{top:2455px;left:150px;width:900px;height:140px}
.quote p{position:absolute;left:60px;right:60px;top:24px;text-align:center;color:var(--green-dark);font-size:20px;font-weight:700;line-height:30px}

/* footer */
.footer{top:2636px;left:0;width:1200px;height:226px;background:var(--green)}
.social{top:56px;left:0;width:1200px;display:flex;justify-content:center;gap:16px}
.social span{width:34px;height:34px;border-radius:50%;background:var(--green-deep)}
.footer .brand{left:0;width:1200px;top:130px;justify-content:center}
.copy{top:2862px;left:0;width:1200px;height:49px;background:var(--green-deep);color:var(--white);font-size:12px;display:flex;align-items:center;justify-content:center;font-weight:500}
</style>
</head>
<body>

<header class="abs topbar">
  <div class="abs contact">P.O Box 218 Fernvale VIC 3100<br>Phone: (03) 9000 1234</div>
  <div class="abs brand"><span class="mark"></span><span class="name">Bluebell Therapy Services</span></div>
  <div class="abs right">E: admin@bluebelltherapy.com.au<br><a href="#">Job Opportunities</a><a href="#">Links</a><a href="#">Contact Us</a></div>
</header>

<nav class="abs nav">
  <a href="#">Occupational Therapy</a><a href="#">Therapy Services</a><a href="#">Group Sessions</a><a href="#">Training Packages</a><a href="#">Meet the Staff</a><a href="#">Fees/ Funding Options</a><a href="#">Parent Resources</a>
</nav>

<section class="abs hero" role="img" aria-label="Photo of a therapist playing with a young boy in a bright therapy room">
  <div class="abs welcome">
    <h1>Welcome to our web site!</h1>
    <p>Bluebell Therapy Services is a specialist Occupational Therapy (OT) provider for children (aged 0-16). Based in Fernvale, Victoria, Bluebell provides comprehensive, private therapy services to children with a broad range of difficulties and disabilities.</p>
  </div>
</section>

<article class="abs svc" style="left:84px;top:712px">
  <h2>Speech Pathology</h2>
  <div class="pic" role="img" aria-label="Photo of a therapist reading with a child" style="background:linear-gradient(135deg,#d9c4a8,#b9413a 60%,#7a8fb0)"></div>
  <p>We work with children to help them learn speech, language, feeding and swallowing skills.</p>
  <a class="btn" href="#">Learn More</a>
</article>
<article class="abs svc" style="left:352px;top:712px">
  <h2>Physical Therapy</h2>
  <div class="pic" role="img" aria-label="Photo of a child exercising with a therapist" style="background:linear-gradient(135deg,#8fb3d6,#d5c3ad 55%,#3b6fa8)"></div>
  <p>We work with children to help them learn to build strength, improve movement and gain functional mobility.</p>
  <a class="btn" href="#">Learn More</a>
</article>
<article class="abs svc" style="left:84px;top:1070px">
  <h2>Occupational Therapy</h2>
  <div class="pic" role="img" aria-label="Photo of children doing a table activity" style="background:linear-gradient(135deg,#e2c58c,#a7643c 55%,#d8b77d)"></div>
  <p>We work with children to help them learn functional skills, including fine motor skills, handwriting, dressing.</p>
  <a class="btn" href="#">Learn More</a>
</article>
<article class="abs svc" style="left:352px;top:1070px">
  <h2>Auxiliary Therapy</h2>
  <div class="pic" role="img" aria-label="Photo of children playing on the floor" style="background:linear-gradient(135deg,#e8dcc2,#c77a4a 50%,#9c8e6a)"></div>
  <p>Specialised therapeutic interventions in which our therapists have gained advanced training.</p>
  <a class="btn" href="#">Learn More</a>
</article>

<section class="abs ot">
  <h2>An Occupational Therapist</h2>
  <p>When a child's ability to be successful in any of these areas is hindered, it can have a dramatic impact on both their self confidence and motivation to persevere. That's where an OT comes in. At Bluebell Therapy Services we assist children who have a learning, social communication or movement based difficulty to be successful in day to day activities including self care, play, leisure and school life.</p>
  <ul>
    <li>Developmental Coordination Disorder (including Dyspraxia)</li>
    <li>Specific learning difficulties</li>
    <li>Acquired brain injuries and brain tumors</li>
    <li>Cerebral palsy</li>
    <li>Autism spectrum disorders (including Asperger's)</li>
    <li>Downs syndrome</li>
    <li>Global developmental delay</li>
  </ul>
</section>
<div class="photo ot-photo" role="img" aria-label="Photo of a therapist helping a child balance on a red exercise ball"></div>

<section class="abs staff" role="img" aria-label="Blurred photo background of a playroom">
  <div class="abs card" style="left:90px"><div class="pic" role="img" aria-label="Portrait photo of staff member with children" style="background:linear-gradient(135deg,#d7b99a,#8b6a52)"></div><div class="label">Hannah Ellery</div></div>
  <div class="abs card" style="left:356px"><div class="pic" role="img" aria-label="Portrait photo of staff member" style="background:linear-gradient(135deg,#e4cdb1,#6f5846)"></div><div class="label">Priya Dawson</div></div>
  <div class="abs card" style="left:624px"><div class="pic" role="img" aria-label="Portrait photo of staff member" style="background:linear-gradient(135deg,#c9a88a,#5e4a3d)"></div><div class="label">Megan Forsyth</div></div>
  <div class="abs card" style="left:889px"><div class="pic" role="img" aria-label="Portrait photo of staff member" style="background:linear-gradient(135deg,#d8b89b,#4e3a30)"></div><div class="label">Leah Whitmore</div></div>
</section>

<section class="abs features">
  <div class="abs fbox" style="left:84px"><h3>Specializing in Apraxia</h3><p>Expert evaluation and treatment of motor speech disorders and articulation skills.</p><a href="#">Read More</a></div>
  <div class="abs fbox" style="left:450px"><h3>Stonebridge Academy</h3><p>Academic development and functional life skills for your child.</p><a href="#">Read More</a></div>
  <div class="abs fbox" style="left:815px"><h3>Teaching &amp; Training</h3><p>We are dedicated to preparing future clinicians to begin their professions.</p><a href="#">Read More</a></div>
</section>

<h2 class="abs section-title" style="left:84px;top:2112px">Family Support Articles</h2>
<article class="abs article" style="left:84px"><div class="pic" role="img" aria-label="Photo of two children playing together" style="background:linear-gradient(135deg,#9ccbe0,#e0c49a)"></div><div class="cap">Speech-Language Are<br>Different</div></article>
<article class="abs article" style="left:350px"><div class="pic" role="img" aria-label="Photo of a smiling girl at mealtime" style="background:linear-gradient(135deg,#f0a7b8,#e6cfa8)"></div><div class="cap">Picky Eater? Help Through<br>Feeding Therapy</div></article>
<article class="abs article" style="left:614px"><div class="pic" role="img" aria-label="Photo of a toddler outdoors" style="background:linear-gradient(135deg,#9bc36a,#d8c8a8)"></div><div class="cap">Autism<br>Treatment</div></article>

<h2 class="abs section-title" style="left:893px;top:2112px">Our Professional Services</h2>
<ul class="abs services-list">
  <li class="active">Paediatric Therapy Services</li>
  <li>Speech and Language</li>
  <li>Occupational Therapy</li>
  <li>Physical Therapy</li>
  <li>Feeding Therapy</li>
  <li>Stonebridge Academy Day Program</li>
  <li>Canine Support</li>
  <li>Clinicians Training &amp; Teaching</li>
</ul>

<section class="abs quote">
  <svg class="abs" style="left:0;top:0" width="40" height="140" viewBox="0 0 40 140" aria-hidden="true"><path d="M34 4 C14 4 20 30 20 50 C20 62 14 68 4 70 C14 72 20 78 20 90 C20 110 14 136 34 136" fill="none" stroke="var(--green-deep)" stroke-width="5"/></svg>
  <p>Kids with special needs are awesome, and we're passionate about your child's potential. Discover our award-winning toys, therapy equipment, classroom tools for special needs and all-inclusive fun!</p>
  <svg class="abs" style="right:0;top:0" width="40" height="140" viewBox="0 0 40 140" aria-hidden="true"><path d="M6 4 C26 4 20 30 20 50 C20 62 26 68 36 70 C26 72 20 78 20 90 C20 110 26 136 6 136" fill="none" stroke="var(--green-deep)" stroke-width="5"/></svg>
</section>

<footer class="abs footer">
  <div class="abs social"><span></span><span></span><span></span><span></span></div>
  <div class="abs brand"><span class="mark"></span><span class="name">Bluebell Therapy Services</span></div>
</footer>
<div class="abs copy">Copyright © 2015 Bluebell Therapy Services. All Reserved</div>

</body>
</html>
```